Bright Meadow Counseling Business Card design with a visually interesting use of Space

I need business cards that are luxurious and give a peaceful, calm vibe. I also had some letterhead designed, and i like the look of it also, it's attached with the logo design for reference/ ideas but feel free to be creative.

Target Market(s)

High end luxurious client who needs counseling

Industry/Entity Type

Marriage and Family Therapy

Contact Information for Business Card

Mira Kowalczyk MS LMFT/ or Toby Hallett address 4150 Larkin Suite 600

Font styles to use
Sans Serif

Colors
0054AA
0677BA
7BADD7
CADEEF
E8F1F8
0094D4
00A9DD
6FCCEA
C7EBF8
E9F6FB
A7469A
B969AE
D3A5CF
EDDBEB
F8F0F9
6B429C
8869AF
B7A5CE
E3DAEB
F3F0F8

Requirements
Must have
• Logo and color scheme but be simple modern and luxurious
Nice to have
• I'd like to incorporate some elelmets from the logo and letterhead into a simple modern card

```html
<!DOCTYPE html>
<html lang="en">
<head>
<meta charset="utf-8">
<title>Bright Meadow Counseling — Business Card</title>
<link href="https://fonts.googleapis.com/css2?family=Open+Sans:wght@300;400;700&display=swap" rel="stylesheet">
<style>
  :root {
    --backdrop: #e4e5e8;
    --teal: #14a89e;
    --white: #ffffff;
    --plum: #a7469a;
    --violet: #8a2f8e;
    --ink: #2f2f33;
    --ink-soft: #4a4a50;
    --icon: #14a89e;
    --wash-lilac: #f3e6f3;
    --wash-blue: #e3eef8;
  }
  * { box-sizing: border-box; margin: 0; padding: 0; }
  html, body { width: 1200px; height: 800px; overflow: hidden; }
  body {
    background: var(--backdrop);
    font-family: "Open Sans", Arial, sans-serif;
    position: relative;
  }
  .card {
    position: absolute;
    width: 525px;
    height: 300px;
    border-radius: 4px;
    box-shadow: 0 10px 24px rgba(0,0,0,0.12);
    overflow: hidden;
  }
  .card--back { left: 48px; top: 250px; background: var(--teal); }
  .card--front { left: 627px; top: 250px; background: var(--white); }

  /* Wordmark */
  .wordmark {
    position: absolute;
    font-weight: 300;
    line-height: 1;
    white-space: nowrap;
  }
  .wordmark__name { display: block; font-size: 44px; letter-spacing: -0.5px; }
  .wordmark__sub { display: block; font-size: 20px; letter-spacing: 5px; margin-top: 4px; padding-left: 70px; }
  .wordmark__dot { position: absolute; border-radius: 50%; }
  .card--back .wordmark { left: 90px; top: 108px; color: var(--white); }
  .card--back .wordmark__dot { width: 46px; height: 46px; right: -62px; top: 6px; background: rgba(255,255,255,0.85); }

  .card--front .wordmark { left: 30px; top: 172px; color: var(--ink); }
  .card--front .wordmark .wordmark__name { font-size: 40px; }
  .card--front .wordmark__dot { width: 40px; height: 40px; right: -56px; top: 6px; background: var(--plum); opacity: 0.85; }

  /* Front details */
  .colour-wash {
    position: absolute;
    right: -30px; top: 40px;
    width: 260px; height: 220px;
    border-radius: 50%;
    background: radial-gradient(ellipse at 40% 45%, var(--wash-blue) 0%, var(--wash-lilac) 45%, rgba(255,255,255,0) 72%);
  }
  .holder {
    position: absolute; left: 30px; top: 20px;
    color: var(--violet);
  }
  .holder__name { font-weight: 700; font-size: 21px; }
  .holder__cred { font-size: 11px; margin-left: 6px; color: var(--plum); }
  .contact {
    position: absolute; left: 30px; top: 60px;
    list-style: none;
    font-size: 14px;
    color: var(--ink-soft);
  }
  .contact li { display: flex; align-items: center; gap: 8px; height: 21px; }
  .contact li.gap { margin-top: 10px; }
  .contact svg { width: 12px; height: 12px; fill: var(--icon); flex: none; }
  .rule {
    position: absolute; left: 0; top: 162px;
    width: 300px; height: 1.5px; background: var(--plum);
  }
  .address {
    position: absolute; right: 28px; bottom: 22px;
    display: flex; align-items: center; gap: 8px;
    font-size: 15px; color: var(--ink);
  }
  .address svg { width: 12px; height: 16px; fill: var(--icon); }
</style>
</head>
<body>

  <section class="card card--back" aria-label="Card back">
    <div class="wordmark">
      <span class="wordmark__name">Bright Meadow</span>
      <span class="wordmark__sub">Counseling</span>
      <span class="wordmark__dot"></span>
    </div>
  </section>

  <section class="card card--front" aria-label="Card front">
    <div class="colour-wash" role="img" aria-label="Soft lilac and blue colour wash"></div>

    <div class="holder">
      <span class="holder__name">Mira Kowalczyk</span><span class="holder__cred">MS LMFT</span>
    </div>

    <ul class="contact">
      <li><svg viewBox="0 0 12 12"><path d="M1 4c0-2 2-3 5-3s5 1 5 3l-2 1-1-1H4L3 5 1 4zM3 6h6l1 5H2z"/></svg>555-214-0386</li>
      <li><svg viewBox="0 0 12 12"><path d="M2 1h8v4H2zM1 6h10v5H1zM3 7v1h6V7z"/></svg>555-318-2741</li>
      <li class="gap"><svg viewBox="0 0 12 12"><path d="M1 2h10v8H1zM2 3l4 3 4-3v-0z"/></svg>hello@brightmeadow.com</li>
      <li><svg viewBox="0 0 12 12"><path d="M6 0a6 6 0 100 12A6 6 0 006 0zm0 2a4 4 0 110 8 4 4 0 010-8z"/></svg>www.brightmeadow.com</li>
    </ul>

    <div class="rule"></div>

    <div class="wordmark">
      <span class="wordmark__name">Bright Meadow</span>
      <span class="wordmark__sub">Counseling</span>
      <span class="wordmark__dot"></span>
    </div>

    <div class="address">
      <svg viewBox="0 0 12 16"><path d="M6 0a6 6 0 00-6 6c0 4 6 10 6 10s6-6 6-10a6 6 0 00-6-6zm0 3.5a2.5 2.5 0 110 5 2.5 2.5 0 010-5z"/></svg>
      4150 Larkin Suite 600
    </div>
  </section>

</body>
</html>
```